A5 front cover for a programme DANCE

To design a front cover for our dance Academy 15th Year anniversary show. The theme is movies and musicals

the school is called Bramblewick Academy of Dance and Performing Arts

venue Harcliffe Playhouse

a5 fornt cover
date 30th June 2019

show title Hold the chorus

Number of Pages Required

1 page

Font styles to use
Sans Serif

Colors

Designer to choose colors to be used in the design.

Requirements
Must have
• up to date fun

```html
<!DOCTYPE html>
<html lang="en">
<head>
<meta charset="utf-8">
<title>Hold the chorus – Programme Cover</title>
<link rel="stylesheet" href="https://fonts.googleapis.com/css2?family=Poppins:wght@400;500;600;700&display=swap">
<style>
  :root {
    --pink: #e4549a;
    --ink: #111111;
    --paper: #ffffff;
    --stage-dark: #1e1619;
    --stage-warm: #4a2e36;
  }
  * { margin: 0; padding: 0; box-sizing: border-box; }
  html, body { width: 835px; height: 1200px; overflow: hidden; background: var(--paper); }
  .cover {
    position: relative;
    width: 835px;
    height: 1200px;
    overflow: hidden;
    background: var(--paper);
    font-family: "Poppins", sans-serif;
    color: var(--ink);
  }
  .hero-photo {
    position: absolute;
    left: 0; top: 0;
    width: 835px; height: 440px;
    background: linear-gradient(180deg, var(--stage-dark) 0%, var(--stage-warm) 100%);
  }
  .film-strip {
    position: absolute;
    left: 0; top: 0;
    width: 835px; height: 1200px;
  }
  .film-strip .band { fill: var(--ink); }
  .film-strip .perforation {
    fill: none;
    stroke: var(--paper);
    stroke-width: 12;
    stroke-dasharray: 12 16;
  }
  .show-title {
    position: absolute;
    left: 0; top: 468px;
    width: 835px;
    text-align: center;
    font-family: "Poppins", sans-serif;
    font-weight: 600;
    font-size: 84px;
    line-height: 1;
    letter-spacing: -1px;
    color: var(--pink);
    transform: rotate(-6deg);
    transform-origin: center;
  }
  .show-details {
    position: absolute;
    left: 0; top: 692px;
    width: 835px;
    text-align: center;
    font-size: 26px;
    line-height: 54px;
  }
  .show-details .label { color: var(--pink); font-weight: 600; }
  .show-details sup { font-size: 14px; }
  .music-notes {
    position: absolute;
    left: 0; top: 0;
    width: 835px; height: 1200px;
    pointer-events: none;
  }
  .music-notes path, .music-notes ellipse { fill: var(--ink); }
  .anniversary-star .star { fill: var(--pink); }
  .anniversary-label {
    position: absolute;
    left: 100px; top: 930px;
    width: 200px;
    text-align: center;
    color: var(--paper);
    font-weight: 600;
    font-size: 25px;
    line-height: 1.1;
    transform: rotate(-14deg);
  }
  .anniversary-label .number { font-size: 40px; }
  .anniversary-label sup { font-size: 18px; }
  .academy-name {
    position: absolute;
    left: 460px; top: 950px;
    width: 330px;
    display: flex;
    align-items: center;
    gap: 14px;
  }
  .academy-name .mark {
    flex: 0 0 22px;
    width: 22px; height: 22px;
    border-radius: 50%;
    background: var(--pink);
  }
  .academy-name .name {
    font-size: 26px;
    font-weight: 500;
    line-height: 1.2;
    color: var(--ink);
  }
</style>
</head>
<body>
<main class="cover">
  <div class="hero-photo" role="img" aria-label="Stage photograph of young dancers in sparkly costumes performing"></div>

  <svg class="film-strip" viewBox="0 0 835 1200" aria-hidden="true">
    <path class="band" d="M0,395 C200,360 420,430 600,390 C700,365 780,300 835,255 L835,560 C760,610 680,640 560,650 C380,665 200,660 0,690 Z"/>
    <path class="perforation" d="M0,418 C200,383 420,453 600,413 C700,388 780,323 835,278"/>
    <path class="perforation" d="M0,667 C200,637 380,642 560,627 C680,617 760,587 835,537"/>
  </svg>

  <h1 class="show-title">hold the chorus</h1>

  <svg class="music-notes" viewBox="0 0 835 1200" aria-hidden="true">
    <g transform="translate(-18 -20)">
      <ellipse cx="82" cy="800" rx="16" ry="12" transform="rotate(-20 82 800)"/>
      <ellipse cx="136" cy="786" rx="16" ry="12" transform="rotate(-20 136 786)"/>
      <path d="M94,798 L94,738 L148,722 L148,784 L144,784 L144,738 L98,750 L98,798 Z"/>
      <path d="M94,738 L148,722 L148,734 L94,750 Z"/>
    </g>
    <g transform="translate(-12 -20)">
      <ellipse cx="698" cy="803" rx="16" ry="12" transform="rotate(-20 698 803)"/>
      <path d="M710,800 L710,730 L714,730 C718,748 740,752 738,775 C732,760 722,756 714,754 L714,800 Z"/>
    </g>
  </svg>

  <section class="show-details">
    <p><span class="label">Where?</span> Harcliffe Playhouse</p>
    <p><span class="label">When?</span> 30<sup>th</sup> June 2019</p>
  </section>

  <svg class="music-notes anniversary-star" viewBox="0 0 835 1200" aria-hidden="true">
    <polygon class="star" points="270,818 265,943 375,948 265,1010 300,1140 215,1055 110,1125 150,1020 35,1035 140,950 90,840 210,920"/>
  </svg>
  <p class="anniversary-label"><span class="number">15<sup>th</sup></span><br>anniversary</p>

  <div class="academy-name">
    <span class="mark"></span>
    <p class="name">Bramblewick Academy of Dance and Performing Arts</p>
  </div>
</main>
</body>
</html>
```